Standard Company Posters / Notices

We have manufacturing sites, across the sites there are notices that managers put up, sometimes like a poster or door notice. These are not in any standard format or follow any standard layout. We wanted to create a notice template that could be adopted with layout guidance for all our internal notices. Some examples of the notices are below. We have three different sites so we would want to interchange the logo to suit the location, I have also added some images used for our values awards as examples of the look we like.

Target Market(s)

Employees

Industry/Entity Type

Food Manufacturing

Requirements
Must have
• Flexible for the site teams to amend to suit their needs.

```html
<!DOCTYPE html>
<html lang="en">
<head>
<meta charset="utf-8">
<title>Site Notices</title>
<link href="https://fonts.googleapis.com/css2?family=Alegreya+Sans:wght@800&family=Marcellus&display=swap" rel="stylesheet">
<style>
  :root {
    --backdrop: #bcbdc0;
    --paper: #f1f1f0;
    --paper-light: #f8f8f7;
    --paper-shade: #e6e6e5;
    --red: #b01f26;
    --red-light: #c4363c;
    --ink: #111111;
    --rule: #9a9a9a;
    --white: #ffffff;
  }
  html, body {
    margin: 0;
    padding: 0;
    width: 854px;
    height: 1200px;
    overflow: hidden;
    background: var(--backdrop);
  }
  .canvas {
    position: relative;
    width: 854px;
    height: 1200px;
  }
  .notice {
    position: absolute;
    left: 56px;
    width: 743px;
    height: 525px;
    overflow: hidden;
  }
  .notice--equipment { top: 56px; }
  .notice--changing { top: 620px; }

  .paper-texture {
    position: absolute;
    inset: 0;
    background: radial-gradient(ellipse at 50% 45%, var(--paper-light) 0%, var(--paper) 55%, var(--paper-shade) 100%);
  }

  .border-band {
    position: absolute;
    left: 0;
    width: 100%;
    height: 22px;
    background: linear-gradient(90deg, var(--red) 0%, var(--red-light) 50%, var(--red) 100%);
  }
  .border-band--top { top: 0; }
  .border-band--bottom { bottom: 0; }

  .ribbon {
    position: absolute;
    left: 50%;
    transform: translateX(-50%);
    background: var(--red);
  }
  .ribbon__label {
    position: absolute;
    inset: 0;
    display: flex;
    align-items: center;
    justify-content: center;
    font-family: "Alegreya Sans", sans-serif;
    font-weight: 800;
    color: var(--white);
    text-transform: uppercase;
    letter-spacing: 0.5px;
    white-space: nowrap;
  }
  .notice--equipment .ribbon { top: 50px; width: 503px; height: 46px; }
  .notice--equipment .ribbon__label { font-size: 42px; }
  .notice--changing .ribbon { top: 72px; width: 549px; height: 62px; }
  .notice--changing .ribbon__label { font-size: 52px; }

  .kit-list {
    position: absolute;
    top: 111px;
    left: 50%;
    transform: translateX(-50%);
    width: 280px;
    margin: 0;
    padding: 0;
    list-style: none;
    font-family: "Marcellus", serif;
    font-size: 30px;
    letter-spacing: 2.5px;
    color: var(--ink);
    text-align: center;
  }
  .kit-list li {
    height: 50.5px;
    line-height: 50px;
    white-space: nowrap;
    border-bottom: 1px dotted var(--rule);
  }
  .kit-list li:last-child { border-bottom: none; }

  .headline {
    position: absolute;
    top: 164px;
    left: 0;
    width: 100%;
    margin: 0;
    font-family: "Alegreya Sans", sans-serif;
    font-weight: 800;
    font-size: 68px;
    line-height: 66px;
    text-align: center;
    color: var(--ink);
    text-transform: uppercase;
  }
  .restriction {
    position: absolute;
    top: 318px;
    left: 0;
    width: 100%;
    margin: 0;
    font-family: "Marcellus", serif;
    font-size: 34px;
    text-align: center;
    color: var(--ink);
    white-space: nowrap;
  }

  .site-mark {
    position: absolute;
    left: 50%;
    transform: translateX(-50%);
    display: flex;
    align-items: center;
    gap: 8px;
    white-space: nowrap;
    font-family: "Alegreya Sans", sans-serif;
    font-weight: 800;
    font-size: 22px;
    color: var(--red);
    text-transform: uppercase;
  }
  .site-mark__square {
    width: 16px;
    height: 16px;
    background: var(--red);
  }
  .notice--equipment .site-mark { top: 426px; }
  .notice--changing .site-mark { top: 426px; }
</style>
</head>
<body>
<div class="canvas">

  <section class="notice notice--equipment">
    <div class="paper-texture" role="img" aria-label="Faint mottled grey paper texture"></div>
    <div class="border-band border-band--top" role="img" aria-label="Red and white diagonal stripe border"></div>
    <div class="ribbon" role="img" aria-label="Red ribbon banner with folded ends">
      <div class="ribbon__label">Block Former Room</div>
    </div>
    <ul class="kit-list">
      <li>1 X Dust Pan</li>
      <li>1 X Brush</li>
      <li>1 X Long Handle</li>
      <li>Brush</li>
      <li>1x Squeegee</li>
    </ul>
    <div class="site-mark"><span class="site-mark__square"></span>Ashdale Creamery</div>
    <div class="border-band border-band--bottom" role="img" aria-label="Red and white diagonal stripe border"></div>
  </section>

  <section class="notice notice--changing">
    <div class="paper-texture" role="img" aria-label="Faint mottled grey paper texture"></div>
    <div class="border-band border-band--top" role="img" aria-label="Red and white diagonal stripe border"></div>
    <div class="ribbon" role="img" aria-label="Red ribbon banner with folded ends">
      <div class="ribbon__label">Female / Visitors</div>
    </div>
    <h1 class="headline">Changing<br>Room Only</h1>
    <p class="restriction">NO MALE DAIRY OPERATIVES</p>
    <div class="site-mark"><span class="site-mark__square"></span>Ashdale Creamery</div>
    <div class="border-band border-band--bottom" role="img" aria-label="Red and white diagonal stripe border"></div>
  </section>

</div>
</body>
</html>
```